Quillfern Nightclub Flyer (Updated)

Flyer for facebook, square is fine, or rectangular. Here is the text:
QUILLFERN
Nightclub + Lounge
presents

SPLIT DECK WEDNESDAY
Nov 29 2018

CLUB FLOOR:
GORDY B2B RALPH
THEODORE BRUSKVIK

LOUNGE:
OTIS B2B HALF TIDE
COPPER FENWICK

Powered by HALVERN Acoustics
4716 Larchmere Avenue 21+ 9pm-2am
quillfernvenue-example.com for VIP booth inquiries

Target Market(s)

Nightclub

Industry/Entity Type

Night Club

Font styles to use
Sans Serif

Colors

Designer to choose colors to be used in the design.

Requirements
Must have
• All the text listed, and plz keep the theme of the attached files. We want to stay consistent with the Quillfern brand
Nice to have
• Try to stay with the theme from the attachments
Should not have
• Dont' stray to far from the general theme we have from the attachments

```html
<!DOCTYPE html>
<html lang="en">
<head>
<meta charset="utf-8">
<title>Quillfern Nightclub – Split Deck Wednesday Flyer</title>
<link rel="stylesheet" href="https://fonts.googleapis.com/css2?family=Mulish:wght@500;700;800&family=Playfair+Display:ital,wght@1,700&family=Cormorant+Garamond:wght@500&display=swap">
<style>
  :root {
    --page-bg: #ececec;
    --flyer-bg: #231f20;
    --gold: #c9935a;
    --gold-light: #f2c27e;
    --gold-dark: #9a6a3a;
    --cream: #f7efe4;
    --cream-deep: #eedfcb;
    --ink: #2a2626;
    --muted: #9a9590;
  }
  * { box-sizing: border-box; margin: 0; padding: 0; }
  html, body { width: 1200px; height: 1200px; overflow: hidden; }
  body {
    background: var(--page-bg);
    font-family: "Mulish", sans-serif;
    color: var(--ink);
    position: relative;
  }
  .flyer {
    position: absolute;
    left: 87px; top: 405px;
    width: 1026px; height: 390px;
    background: var(--flyer-bg);
    overflow: hidden;
    box-shadow: 0 10px 30px rgba(0,0,0,.25);
  }
  .ornament-area {
    position: absolute;
    left: 0; top: 50px;
    width: 240px; height: 340px;
    background: radial-gradient(circle at 0% 100%, var(--gold-light) 0%, var(--gold) 35%, var(--gold-dark) 62%, rgba(154,106,58,0) 72%);
    opacity: .85;
  }
  .ticket-frame { position: absolute; left: 0; top: 0; width: 1026px; height: 390px; }
  .content { position: absolute; inset: 0; }
  .brand {
    position: absolute; left: 456px; top: 52px; width: 400px;
    text-align: center;
  }
  .brand-name {
    font-family: "Mulish", sans-serif;
    font-weight: 500;
    font-size: 50px;
    letter-spacing: 2px;
    line-height: 1;
    color: var(--ink);
  }
  .brand-tag {
    font-size: 12px; font-weight: 500;
    letter-spacing: 3px; color: var(--muted);
    margin-top: 6px;
  }
  .presents {
    font-family: "Playfair Display", serif;
    font-style: italic; font-weight: 700;
    font-size: 19px; margin-top: 0;
    color: var(--ink);
  }
  .lineup-col {
    position: absolute; top: 167px; width: 240px;
    text-align: center;
    font-weight: 800; font-size: 16px; line-height: 22px;
    text-transform: uppercase;
  }
  .lineup-col .label { color: var(--gold); }
  .col-date { left: 309px; }
  .col-date .date { text-transform: none; }
  .col-club { left: 494px; }
  .col-lounge { left: 702px; }
  .flourish {
    display: block; margin: 8px auto 0;
    width: 48px; height: 12px; border-radius: 6px;
    background: linear-gradient(90deg, rgba(201,147,90,0), var(--gold) 50%, rgba(201,147,90,0));
  }
  .venue-info {
    position: absolute; left: 366px; top: 278px; width: 300px;
    text-align: center; font-weight: 700; font-size: 16px; line-height: 22px;
  }
  .venue-info .web { color: var(--gold); }
  .powered {
    position: absolute; left: 697px; top: 288px; width: 200px;
    text-align: center; font-weight: 800; font-size: 16px;
  }
  .sponsor {
    display: flex; align-items: center; justify-content: center; gap: 8px;
    margin-top: 4px;
  }
  .sponsor .rule { width: 40px; height: 1px; background: var(--ink); }
  .sponsor-name { font-weight: 800; font-size: 20px; letter-spacing: 3px; color: var(--ink); }
</style>
</head>
<body>
  <section class="flyer" aria-label="Quillfern Nightclub Split Deck Wednesday flyer">
    <div class="ornament-area" role="img" aria-label="Gold mandala ornament"></div>

    <svg class="ticket-frame" viewBox="0 0 1026 390" aria-hidden="true">
      <defs>
        <linearGradient id="goldEdge" x1="0" y1="0" x2="1" y2="1">
          <stop offset="0" stop-color="#9a6a3a"/>
          <stop offset=".45" stop-color="#f2c27e"/>
          <stop offset=".7" stop-color="#c9935a"/>
          <stop offset="1" stop-color="#f5cf90"/>
        </linearGradient>
        <linearGradient id="marble" x1="0" y1="0" x2="1" y2="1">
          <stop offset="0" stop-color="#f9f3ea"/>
          <stop offset=".5" stop-color="#f1e4d2"/>
          <stop offset="1" stop-color="#f8f0e6"/>
        </linearGradient>
      </defs>
      <polygon fill="url(#goldEdge)" points="381,24 931,24 931,70 975,70 975,317 931,317 931,361 381,361 381,317 337,317 337,70 381,70"/>
      <polygon fill="url(#marble)" points="389,32 923,32 923,78 967,78 967,309 923,309 923,353 389,353 389,309 345,309 345,78 389,78"/>
      <rect x="355" y="40" width="597" height="305" fill="none" stroke="#c9935a" stroke-width="1"/>
    </svg>

    <div class="content">
      <header class="brand">
        <div class="brand-name">QUILLFERN</div>
        <div class="brand-tag">NIGHTCLUB + LOUNGE</div>
        <div class="presents">presents</div>
      </header>

      <div class="lineup-col col-date">
        <div class="label">Split Deck</div>
        <div>Wednesday</div>
        <div class="date">Nov 29 2018</div>
        <span class="flourish" role="img" aria-label="Gold flourish"></span>
      </div>

      <div class="lineup-col col-club">
        <div class="label">Club Floor:</div>
        <div>Gordy B2B Ralph</div>
        <div>Theodore Bruskvik</div>
        <span class="flourish" role="img" aria-label="Gold flourish"></span>
      </div>

      <div class="lineup-col col-lounge">
        <div class="label">Lounge:</div>
        <div>Otis B2B Half Tide</div>
        <div>Copper Fenwick</div>
        <span class="flourish" role="img" aria-label="Gold flourish"></span>
      </div>

      <div class="venue-info">
        <div>4716 Larchmere Avenue 21+9pm-2am</div>
        <div class="web">quillfernvenue-example.com</div>
        <div>for VIP booth inquiries</div>
      </div>

      <div class="powered">
        <div>Powered by</div>
        <div class="sponsor">
          <span class="rule"></span>
          <span class="sponsor-name">HALVERN</span>
          <span class="rule"></span>
        </div>
      </div>
    </div>
  </section>
</body>
</html>
```